Chat Nest Landing page for Buyers of New Construction Luxury Homes

Mirela Dunstan Real Estate Group powered by Brockhaven Partners Realty

must have the equal housing logo at the bottom of the page.

Take a look at http://www.chatnest.example/orbitguardcorps We are looking for something as elaborate as this.

We need a Chat Nest Fan Page created to attract home buyers looking at Newly Constructed homes. They need to feel that we are the experts and can save them money and at the same time our service is actually free to them. They must feel we are not just realtors but experts in fighting for them. You can visit www.quillbarrowpath.example for a short video that conveys the point. We will drive them to this landing page to capture their info.

The landing page should have the following copy:

We guarantee that we will save buyers money. We’ll pay up to $10,000 if we cannot save them money!
2. "Like" our Chatnest Fan Page we want to drive people to like our fan page to learn about how to Buy Newly Constructed Homes
embed the video you see on the link above onto the site.

We have a radio spot we would like to incorporate onto the page if possible

Must have a luxury, professional, tasteful, classy look.

age 30+ income of 100k+ Living in the washington dc, northern virginia area

Radio

• pictures of luxury homes, townhouses and even condos

```html
<!DOCTYPE html>
<html lang="en">
<head>
<meta charset="utf-8">
<title>Mirela Dunstan Real Estate Group – Buying New Construction</title>
<link href="https://fonts.googleapis.com/css2?family=Baloo+2:wght@500;600;700&family=Arimo:wght@400&display=swap" rel="stylesheet">
<style>
  :root {
    --page-bg: #ffffff;
    --brand-red: #7a1108;
    --brand-red-dark: #4e0a05;
    --label-red: #7b1712;
    --accent-red: #8b1a10;
    --panel-grey: #e7e7e7;
    --text-light: #ececec;
    --like-blue: #8fa9e6;
    --video-bar: #3b6b96;
    --control-grey: #ededed;
    --badge-dark: #2a2a2a;
  }
  * { margin: 0; padding: 0; box-sizing: border-box; }
  html, body { width: 900px; height: 1200px; overflow: hidden; background: var(--page-bg); }
  body { position: relative; font-family: "Baloo 2", sans-serif; }

  .landing {
    position: absolute; left: 195px; top: 75px; width: 511px; height: 1049px;
    background: var(--panel-grey);
    border: 2px solid var(--brand-red);
  }
  .hero {
    position: absolute; left: -2px; top: -2px; width: 511px; height: 385px;
    background: linear-gradient(180deg, var(--brand-red-dark) 0%, var(--brand-red) 22%, var(--brand-red) 100%);
    box-shadow: 0 12px 14px -6px rgba(0,0,0,.45);
    color: var(--text-light); text-align: center;
  }
  .brand {
    position: absolute; left: 30px; top: 38px; display: flex; align-items: center; gap: 12px;
  }
  .brand-dot { width: 22px; height: 22px; border-radius: 50%; background: #9a9a9a; }
  .brand-name { font-size: 40px; font-weight: 700; color: #ffffff; line-height: 48px; }
  .like-prompt {
    position: absolute; left: 286px; top: 30px; display: flex; gap: 14px; align-items: flex-start;
    text-align: left;
  }
  .like-icon { width: 46px; height: 40px; margin-top: 4px; background: #6f88c8; border-radius: 4px; }
  .like-copy { font-size: 14px; line-height: 15px; font-weight: 600; color: #f2f2f2; margin-top: 1px; }
  .like-copy .like-link { color: var(--like-blue); }
  .guarantee { position: absolute; top: 145px; width: 100%; font-size: 35px; line-height: 36px; font-weight: 600; }
  .payout-lead { position: absolute; top: 237px; width: 100%; font-size: 26px; line-height: 30px; font-weight: 600; }
  .payout-amount { position: absolute; top: 262px; width: 100%; font-size: 64px; line-height: 64px; font-weight: 600; letter-spacing: -1px; }
  .payout-tail { position: absolute; top: 319px; width: 100%; font-size: 26px; line-height: 30px; font-weight: 600; }

  .video-player {
    position: absolute; left: 29px; top: 419px; width: 449px; height: 272px;
    background: #fff; box-shadow: 0 10px 12px -4px rgba(0,0,0,.35);
  }
  .video-title {
    height: 32px; background: var(--video-bar); color: #fff;
    font-family: "Arimo", sans-serif; font-size: 16px; line-height: 32px; padding-left: 11px;
  }
  .video-frame {
    position: relative; height: 194px;
    background: linear-gradient(180deg, #79b6ea 0%, #c9dcea 45%, #d9cfc4 70%, #7d9a5a 100%);
  }
  .video-frame .play {
    position: absolute; left: 195px; top: 68px; width: 58px; height: 38px;
    background: rgba(30,30,30,.85); border-radius: 6px;
  }
  .video-controls {
    position: absolute; left: 0; bottom: 0; width: 100%; height: 32px;
    background: linear-gradient(#fafafa, var(--control-grey)); border-top: 1px solid #ccc;
    display: flex; align-items: center; font-family: "Arimo", sans-serif; font-size: 11px; color: #555;
  }
  .video-controls .ctrl { width: 30px; height: 100%; border-right: 1px solid #ccc; display: flex; align-items: center; justify-content: center; }
  .video-controls .time { padding-left: 10px; flex: 1; }
  .video-controls .host { padding: 0 8px; border-left: 1px solid #ccc; height: 100%; line-height: 32px; color: #444; }

  .radio-spot { position: absolute; left: 24px; top: 731px; display: flex; align-items: center; gap: 11px; }
  .radio-button { width: 49px; height: 49px; }
  .radio-label { font-size: 24px; font-weight: 600; color: var(--accent-red); }

  .service-tiles { position: absolute; left: 29px; top: 810px; display: flex; gap: 6px; }
  .tile { width: 145px; }
  .tile-photo { height: 118px; }
  .tile-label {
    margin-top: 6px; height: 22px; background: var(--label-red); color: #fff;
    text-align: center; font-size: 16px; font-weight: 600; line-height: 24px;
  }
  .photo-buy { background: linear-gradient(180deg, #a9cce8 0%, #e6d28c 45%, #5f8a3c 100%); }
  .photo-sell { background: linear-gradient(180deg, #6f9fd3 0%, #dfe3e6 55%, #8aa36a 100%); }
  .photo-finance { background: linear-gradient(180deg, #7fb1e2 0%, #d7d2c8 50%, #8fb4c2 100%); }

  .compliance { position: absolute; left: 193px; top: 996px; display: flex; gap: 6px; align-items: center; }
  .compliance span { display: block; background: var(--badge-dark); }
  .badge-square { width: 22px; height: 26px; }
  .badge-house { width: 26px; height: 26px; border-radius: 2px; }
  .badge-listing { width: 48px; height: 22px; border-radius: 2px; }
</style>
</head>
<body>
<main class="landing">
  <header class="hero">
    <div class="brand">
      <span class="brand-dot"></span>
      <span class="brand-name">Mirela</span>
    </div>
    <div class="like-prompt">
      <div class="like-icon"></div>
      <p class="like-copy">click the <span class="like-link">Like Button</span><br>to learn more about<br>how to Buy Newly<br>Constructed Homes</p>
    </div>
    <h1 class="guarantee">We guarantee that we<br>will save buyers money.</h1>
    <p class="payout-lead">We’ll pay up to</p>
    <p class="payout-amount">$10,000</p>
    <p class="payout-tail">if we cannot save them money!</p>
  </header>

  <section class="video-player">
    <div class="video-title">Dale Renwick -&nbsp; Buying New Construction</div>
    <div class="video-frame" role="img" aria-label="Couple seen from behind looking at a large new-construction house">
      <svg class="play" viewBox="0 0 58 38"><path d="M24 11 L36 19 L24 27 Z" fill="#fff"/></svg>
    </div>
    <div class="video-controls">
      <div class="ctrl"><svg width="12" height="12" viewBox="0 0 12 12"><path d="M2 1 L11 6 L2 11 Z" fill="#555"/></svg></div>
      <div class="ctrl"><svg width="16" height="12" viewBox="0 0 16 12"><path d="M1 4 H4 L8 1 V11 L4 8 H1 Z" fill="#555"/></svg></div>
      <div class="time">0:00 / 2:49</div>
      <div class="ctrl" style="border-left:1px solid #ccc"><svg width="12" height="12" viewBox="0 0 12 12"><path d="M5 0 H7 V5 H12 V7 H7 V12 H5 V7 H0 V5 H5 Z" fill="#555"/></svg></div>
      <div class="host">ViewReel</div>
      <div class="ctrl" style="border-left:1px solid #ccc;border-right:0"><svg width="14" height="14" viewBox="0 0 14 14" fill="none" stroke="#555" stroke-width="2"><path d="M1 5V1H5M9 1H13V5M13 9V13H9M5 13H1V9"/></svg></div>
    </div>
  </section>

  <a class="radio-spot">
    <svg class="radio-button" viewBox="0 0 49 49">
      <circle cx="24.5" cy="24.5" r="23" fill="#d8d8d8" stroke="#aaa"/>
      <circle cx="24.5" cy="24.5" r="19" fill="#c5200f"/>
      <path d="M20 14 L32 24.5 L20 35 Z" fill="#f2f2f2"/>
    </svg>
    <span class="radio-label">Click Here to listen to our Radio Spot</span>
  </a>

  <nav class="service-tiles">
    <div class="tile"><div class="tile-photo photo-buy" role="img" aria-label="Yellow Victorian house with green roof and blossoming tree"></div><div class="tile-label">Buy</div></div>
    <div class="tile"><div class="tile-photo photo-sell" role="img" aria-label="White house with grey roof behind a picket fence"></div><div class="tile-label">Sell</div></div>
    <div class="tile"><div class="tile-photo photo-finance" role="img" aria-label="Modern luxury home with pool"></div><div class="tile-label">Finance</div></div>
  </nav>

  <footer class="compliance" aria-label="Realtor, equal housing and listing service badges">
    <span class="badge-square"></span>
    <span class="badge-house"></span>
    <span class="badge-listing"></span>
  </footer>
</main>
</body>
</html>
```